Simple and Approachable Cover for Pet Expo Company Page

Size: 2000 x 430; looking simply for words "Dunmore HR Consulting" and email address "DunmoreHRConsulting@brelvamail.com." This is for a cover photo for a company profile page for the Hollow Oak Expo, where I am a featured speaker on Employee Communications later this month. You can incorporate the attached photo to the left of the banner ad if you wish. The mood I wish to present is approachable, positive and simple.

Target Market(s)

small pet retail business owners

Industry/Entity Type

Pet Shop

Font styles to use
Serif
Sans Serif

Requirements
Must have
• Email address clearly defined/separated. Easy to read.
Nice to have
• I like the picture that I included; subtle pet paw background is also nice
Should not have
• No paid stock images

```html
<!DOCTYPE html>
<html lang="en">
<head>
<meta charset="utf-8">
<title>Dunmore HR Consulting</title>
<link rel="stylesheet" href="https://fonts.googleapis.com/css2?family=Poppins:wght@500&family=Inter:wght@400&display=swap">
<style>
  :root {
    --bg: #f3f3f3;
    --scene-light: #ebebeb;
    --scene-mid: #dedede;
    --scene-dark: #d2d2d2;
    --brand-blue: #0a63d8;
    --ink: #1f1f1f;
    --photo-warm: #c99a63;
    --photo-red: #d8242c;
    --photo-blue: #5879a8;
  }
  * { margin: 0; padding: 0; box-sizing: border-box; }
  html, body { width: 1200px; height: 258px; overflow: hidden; background: var(--bg); }
  .cover {
    position: relative;
    width: 1200px;
    height: 258px;
    background: var(--bg);
    overflow: hidden;
  }
  .city-backdrop {
    position: absolute;
    inset: 0;
    width: 1200px;
    height: 258px;
  }
  .team-photo {
    position: absolute;
    left: 60px;
    top: 0;
    width: 446px;
    height: 258px;
    background: linear-gradient(100deg, var(--photo-warm) 0%, var(--photo-blue) 30%, var(--photo-red) 55%, var(--photo-blue) 70%, var(--photo-warm) 88%, var(--scene-mid) 100%);
    border-radius: 40px 40px 0 0;
    opacity: 0.9;
  }
  .brand {
    position: absolute;
    left: 575px;
    top: 60px;
  }
  .brand-name {
    font-family: "Poppins", sans-serif;
    font-weight: 500;
    font-size: 51px;
    line-height: 1;
    color: var(--brand-blue);
    letter-spacing: -0.3px;
  }
  .contact {
    display: flex;
    align-items: center;
    gap: 12px;
    margin-top: 15px;
    margin-left: 0;
  }
  .contact-icon { width: 34px; height: 34px; flex: none; }
  .contact-email {
    font-family: "Inter", sans-serif;
    font-weight: 400;
    font-size: 25px;
    color: var(--ink);
    letter-spacing: -0.3px;
  }
</style>
</head>
<body>
  <main class="cover">
    <svg class="city-backdrop" viewBox="0 0 1200 258" aria-hidden="true">
      <rect x="450" y="65" width="45" height="150" fill="var(--scene-light)"/>
      <rect x="493" y="65" width="42" height="160" fill="var(--scene-mid)" opacity="0.6"/>
      <rect x="550" y="90" width="40" height="130" fill="var(--scene-light)"/>
      <rect x="870" y="65" width="50" height="150" fill="var(--scene-light)"/>
      <rect x="1040" y="170" width="50" height="60" fill="var(--scene-light)"/>
      <ellipse cx="660" cy="165" rx="90" ry="50" fill="var(--scene-light)"/>
      <ellipse cx="760" cy="170" rx="70" ry="45" fill="var(--scene-light)"/>
      <ellipse cx="20" cy="140" rx="60" ry="60" fill="var(--scene-light)"/>
      <path d="M480 240 C600 228 720 228 840 240 C950 225 1080 225 1200 240 L1200 258 L480 258 Z" fill="var(--scene-mid)" opacity="0.6"/>
      <rect x="480" y="245" width="720" height="13" fill="var(--scene-dark)" opacity="0.5"/>
    </svg>

    <div class="team-photo" role="img" aria-label="Photo of the two consultants seated outdoors with their two hound dogs"></div>

    <section class="brand">
      <h1 class="brand-name">Dunmore HR Consulting</h1>
      <p class="contact">
        <svg class="contact-icon" viewBox="0 0 34 34" aria-hidden="true">
          <circle cx="17" cy="17" r="15.5" fill="none" stroke="var(--brand-blue)" stroke-width="2"/>
          <circle cx="17" cy="17" r="12.5" fill="var(--brand-blue)"/>
          <rect x="9.5" y="12" width="15" height="10" fill="#fff"/>
          <path d="M9.5 12 L17 18 L24.5 12" fill="none" stroke="var(--brand-blue)" stroke-width="1.4"/>
        </svg>
        <span class="contact-email">DunmoreHRConsulting@brelvamail.com</span>
      </p>
    </section>
  </main>
</body>
</html>
```